Medical equipment business looking for professional, unique business card

We need a business card design for a durable medical equipment company. We are small but would like our cards to express that we are much bigger. We focus on braces (back, knee, wrist, etc) but also do crutches, rollators, wheelchairs- basically medical equipment that gets you going and back in Action. Our colors are blue and green and our logo has an arrow and use of a "spine". We'd like to express professionalism while being unique.

Industry/Entity Type

Medical Equipment

Contact Information for Business Card

Professional feel but unique. Memorable.

Font styles to use
Serif
Sans Serif
Other font styles liked:
• verdana

Requirements
Must have
• card holders cell#, business phone#, fax#, email, website address, business address, logo
Nice to have
• use of medical/healthcare related descriptive words, items, look
Should not have
• the wrong colors or cartoon characters.

```html
<!DOCTYPE html>
<html lang="en">
<head>
<meta charset="utf-8">
<title>Keystone DME – Business Card</title>
<link href="https://fonts.googleapis.com/css2?family=Roboto:wght@400;500;700&display=swap" rel="stylesheet">
<style>
  :root {
    --navy: #0b3f63;
    --navy-deep: #083552;
    --green: #8cc63f;
    --sky: #1b8fcf;
    --ink: #0e4a75;
    --grey: #777777;
    --white: #ffffff;
    --stage: #e4e6e8;
  }
  * { margin: 0; padding: 0; box-sizing: border-box; }
  html, body { width: 1200px; height: 1000px; overflow: hidden; }
  body { background: var(--stage); font-family: 'Roboto', Arial, sans-serif; position: relative; }

  .card { position: absolute; left: 220px; width: 760px; overflow: hidden; box-shadow: 0 4px 14px rgba(0,0,0,.25); }
  .card-front { top: 50px; height: 433px; background: linear-gradient(135deg, var(--navy-deep) 0%, var(--navy) 60%, #145a83 100%); }
  .card-back { top: 523px; height: 435px; background: var(--white); }

  .front-brand { position: absolute; left: 0; right: 0; top: 132px; text-align: center; }
  .front-brand .brand-name { color: var(--white); font-size: 72px; font-weight: 500; letter-spacing: 1px; line-height: 1; }
  .front-brand .brand-tagline { color: var(--sky); font-size: 27px; font-weight: 500; margin-top: 28px; }

  .product-list { position: absolute; left: 0; right: 0; top: 368px; display: flex; justify-content: center; gap: 10px; list-style: none; }
  .product-list li { color: var(--white); font-size: 17px; display: flex; align-items: center; gap: 5px; }
  .product-list li::before { content: ""; width: 9px; height: 9px; border-radius: 50%; background: var(--green); }

  .back-wave { position: absolute; inset: 0; }

  .name-tab { position: absolute; left: 0; top: 60px; width: 14px; height: 44px; background: var(--green); border-radius: 0 6px 6px 0; }
  .holder { position: absolute; left: 42px; top: 58px; }
  .holder-name { color: var(--sky); font-size: 23px; font-weight: 500; }
  .holder-title { color: var(--grey); font-size: 17px; margin-top: 4px; }

  .back-brand { position: absolute; left: 44px; top: 292px; }
  .back-brand .brand-name { color: var(--ink); font-size: 44px; font-weight: 500; line-height: 1; }
  .back-brand .brand-tagline { color: var(--sky); font-size: 17px; font-weight: 500; margin-top: 20px; margin-left: 104px; }

  .contact { position: absolute; left: 490px; top: 104px; color: var(--white); font-size: 17px; }
  .contact-company { color: var(--green); font-weight: 700; font-size: 17px; margin-bottom: 8px; }
  .contact-address { line-height: 22px; margin-bottom: 18px; }
  .contact-lines { list-style: none; }
  .contact-lines li { display: flex; align-items: center; gap: 8px; height: 24.5px; }
  .contact-lines svg { width: 12px; height: 12px; fill: var(--green); flex: none; }
</style>
</head>
<body>

<section class="card card-front">
  <div class="front-brand">
    <div class="brand-name">Keystone DME</div>
    <div class="brand-tagline">Durable Medical Equipment</div>
  </div>
  <ul class="product-list">
    <li>Back</li><li>Knee</li><li>Wrist</li><li>Crutches</li><li>Rollators</li><li>Wheelchairs</li>
  </ul>
</section>

<section class="card card-back">
  <svg class="back-wave" viewBox="0 0 760 435" width="760" height="435">
    <path d="M312 0 C 300 150, 430 240, 438 435 L760 435 L760 0 Z" fill="var(--green)"/>
    <path d="M330 0 C 320 150, 448 240, 456 435 L760 435 L760 0 Z" fill="var(--navy)"/>
  </svg>

  <div class="name-tab"></div>
  <div class="holder">
    <div class="holder-name">Daniel Reed</div>
    <div class="holder-title">President</div>
  </div>

  <div class="back-brand">
    <div class="brand-name">Keystone DME</div>
    <div class="brand-tagline">Durable Medical Equipment</div>
  </div>

  <div class="contact">
    <div class="contact-company">Keystone DME</div>
    <div class="contact-address">Street name, Suite 100<br>State, Zip Code, Country</div>
    <ul class="contact-lines">
      <li><svg viewBox="0 0 12 12"><path d="M2 1 L4.5 1 L5.3 3.6 L3.9 4.6 C4.6 6 6 7.4 7.4 8.1 L8.4 6.7 L11 7.5 L11 10 C11 10.6 10.6 11 10 11 C5.3 11 1 6.7 1 2 C1 1.4 1.4 1 2 1 Z"/></svg>012 345 6789</li>
      <li><svg viewBox="0 0 12 12"><path d="M3.5 0.5 H8.5 A1 1 0 0 1 9.5 1.5 V10.5 A1 1 0 0 1 8.5 11.5 H3.5 A1 1 0 0 1 2.5 10.5 V1.5 A1 1 0 0 1 3.5 0.5 Z M3.8 2 V9 H8.2 V2 Z M6 9.7 A0.6 0.6 0 1 0 6 10.9 A0.6 0.6 0 1 0 6 9.7 Z"/></svg>012 345 6789</li>
      <li><svg viewBox="0 0 12 12"><path d="M3 0.5 H9 V3.5 H3 Z M1 4.5 H11 V9 H9 V11.5 H3 V9 H1 Z M4 8 V10.5 H8 V8 Z"/></svg>012 345 6789</li>
      <li><svg viewBox="0 0 12 12"><path d="M0.5 2 H11.5 V10 H0.5 Z M1.5 3 L6 6.5 L10.5 3 Z"/></svg>info@yourwebsite.com</li>
      <li><svg viewBox="0 0 12 12"><path d="M6 0.5 A5.5 5.5 0 1 0 6 11.5 A5.5 5.5 0 1 0 6 0.5 Z M6 1.6 C7 2.6 7.5 4 7.6 5.4 H4.4 C4.5 4 5 2.6 6 1.6 Z M1.7 6.6 H3.4 C3.5 8 3.9 9.3 4.6 10.2 C3.1 9.7 1.9 8.3 1.7 6.6 Z M1.7 5.4 C1.9 3.7 3.1 2.3 4.6 1.8 C3.9 2.7 3.5 4 3.4 5.4 Z M4.4 6.6 H7.6 C7.5 8 7 9.4 6 10.4 C5 9.4 4.5 8 4.4 6.6 Z M8.6 6.6 H10.3 C10.1 8.3 8.9 9.7 7.4 10.2 C8.1 9.3 8.5 8 8.6 6.6 Z M8.6 5.4 C8.5 4 8.1 2.7 7.4 1.8 C8.9 2.3 10.1 3.7 10.3 5.4 Z"/></svg>www.yourwebsite.com</li>
    </ul>
  </div>
</section>

</body>
</html>
```